Business Card for TOV

We need a Corporate style business card for a new Industrial recycling company based in Australia. We recycle industrial products from Mining companies, power stations and other large industry all around the country.

We want the card to represent a modern, innovative professional company that is an industry leader.

We want the card to be double sided. I think with the logo centred by itself on one side and the text displayed with all our details on the other side.

(or you could put the persons name with the job title on the side with the logo?? I'll leave that up to your creative sides)

Open to how you divide and place the information on the one side of the card.

I think the persons name and the title should have its own place. The rest of the information can be placed as you think is best and then I will provide feedback as to what I think works best.

I have attached the logo file so you can add that to the one side. Whether you use it in a smaller form on the second side too is an option but I'll leave that up to you initially?

Information required on the card is as follows

Dermot Halloran
Director

0438 972 506

dermot@tovq.com.au

Po Box 782
Brindle ACT 2694

www.tovq.com.au

ACN 582 917 306 (This can be in very small print and can be in the bottom corner of the card or somewhere not very prominent

Wanted to thank everyone for their submissions. 

We were really torn on about 5 designs in the end.

We decided to go with the first one we liked.

We have another company that is going to need logo and business card design in the coming weeks.

I will save your designer ID's so I can invite you all to that project. too!

Thanks again and all the best

Dermot

Target Market(s)

Corporate and medium to large business clients

Industry/Entity Type

Industrial

```html
<!DOCTYPE html>
<html lang="en">
<head>
<meta charset="utf-8">
<title>TOV Business Card</title>
<link rel="stylesheet" href="https://fonts.googleapis.com/css2?family=Open+Sans:wght@400;700&family=Fredoka:wght@600&display=swap">
<style>
  :root {
    --board: #e4e1dc;
    --card: #ffffff;
    --ink: #2d2d2d;
    --charcoal: #333233;
    --lime: #8dc63f;
    --sky: #2a9ad0;
    --silver: #d0d0d0;
    --forest: #3f9a44;
    --row: #e6e6e8;
    --label: #3a3a3a;
  }
  * { box-sizing: border-box; margin: 0; padding: 0; }
  html, body { width: 1200px; height: 900px; overflow: hidden; }
  body { background: var(--board); position: relative; font-family: "Open Sans", sans-serif; }

  .side-label {
    position: absolute; font-family: "Open Sans", sans-serif; font-weight: 400;
    font-size: 52px; color: var(--label);
  }
  .side-label--front { left: 150px; top: 146px; }
  .side-label--back { left: 143px; top: 604px; }

  .card { position: absolute; background: var(--card); overflow: hidden; }
  .card--front { left: 473px; top: 27px; width: 687px; height: 391px; }
  .card--back { left: 473px; top: 465px; width: 689px; height: 395px; }
  .card svg.bands { position: absolute; inset: 0; }

  .brand { position: absolute; display: flex; align-items: center; gap: 34px; }
  .brand__dot { width: 140px; height: 140px; border-radius: 50%; background: var(--lime); }
  .brand__name {
    font-family: "Open Sans", sans-serif; font-weight: 700; font-size: 78px;
    letter-spacing: 6px; color: var(--ink); line-height: 1;
  }
  .card--front .brand { left: 48px; top: 108px; }
  .card--back .brand { left: 74px; top: 70px; }

  .holder { position: absolute; left: 44px; top: 284px; width: 240px; text-align: center; color: #fff; }
  .holder__name { font-family: "Fredoka", sans-serif; font-weight: 600; font-size: 25px; letter-spacing: 0.5px; line-height: 1; }
  .holder__role { font-size: 15px; margin-top: 3px; }

  .contact { position: absolute; right: 106px; text-align: right; font-weight: 700; font-size: 13px; line-height: 17px; color: var(--ink); }
  .contact--web { top: 254px; }
  .contact--post { top: 305px; }
  .icon { position: absolute; right: 44px; }
  .icon--screen { top: 257px; }
  .icon--phone { top: 309px; }

  .acn { position: absolute; left: 5px; bottom: 2px; font-size: 10px; color: #fff; }
</style>
</head>
<body>
  <div class="side-label side-label--front">front</div>
  <div class="side-label side-label--back">Back</div>

  <section class="card card--front">
    <svg class="bands" width="687" height="391" viewBox="0 0 687 391">
      <polygon points="0,348 350,348 378,391 0,391" fill="var(--charcoal)"/>
      <polygon points="347,348 427,348 455,391 375,391" fill="var(--lime)"/>
      <polygon points="427,348 507,348 535,391 455,391" fill="var(--sky)"/>
      <polygon points="507,348 585,348 613,391 535,391" fill="var(--silver)"/>
      <polygon points="585,348 687,348 687,391 613,391" fill="var(--forest)"/>
    </svg>
    <div class="brand">
      <span class="brand__dot"></span>
      <span class="brand__name">TOV</span>
    </div>
  </section>

  <section class="card card--back">
    <svg class="bands" width="689" height="395" viewBox="0 0 689 395">
      <rect x="250" y="248" width="439" height="47" fill="var(--row)"/>
      <rect x="250" y="300" width="439" height="45" fill="var(--row)"/>
      <polygon points="0,248 272,248 377,395 0,395" fill="var(--charcoal)"/>
      <polygon points="347,350 427,350 459,395 379,395" fill="var(--lime)"/>
      <polygon points="427,350 507,350 539,395 459,395" fill="var(--sky)"/>
      <polygon points="507,350 585,350 617,395 539,395" fill="var(--silver)"/>
      <polygon points="585,350 689,350 689,395 617,395" fill="var(--forest)"/>
    </svg>
    <div class="brand">
      <span class="brand__dot"></span>
      <span class="brand__name">TOV</span>
    </div>

    <div class="holder">
      <div class="holder__name">DERMOT HALLORAN</div>
      <div class="holder__role">Director</div>
    </div>

    <div class="contact contact--web">dermot@tovq.com.au<br>www.tovq.com.au</div>
    <svg class="icon icon--screen" width="34" height="28" viewBox="0 0 34 28" aria-hidden="true">
      <rect x="2" y="2" width="30" height="19" fill="none" stroke="var(--ink)" stroke-width="3"/>
      <rect x="14" y="21" width="6" height="4" fill="var(--ink)"/>
      <rect x="9" y="25" width="16" height="3" fill="var(--ink)"/>
    </svg>

    <div class="contact contact--post">0438 972 506<br>Po Box 782 Brindle ACT 2694</div>
    <svg class="icon icon--phone" width="34" height="28" viewBox="0 0 34 28" aria-hidden="true">
      <path d="M2 9 Q17 -1 32 9 L29 13 L23 11 L23 7 Q17 5 11 7 L11 11 L5 13 Z" fill="var(--ink)"/>
      <path d="M9 14 L25 14 L31 27 L3 27 Z" fill="var(--ink)"/>
      <g fill="var(--row)">
        <rect x="12" y="17" width="2" height="2"/><rect x="16" y="17" width="2" height="2"/><rect x="20" y="17" width="2" height="2"/>
        <rect x="12" y="21" width="2" height="2"/><rect x="16" y="21" width="2" height="2"/><rect x="20" y="21" width="2" height="2"/>
      </g>
    </svg>

    <div class="acn">ACN 582 917 306</div>
  </section>
</body>
</html>
```